Lorna Pettibone Nook Charmer

a larger business card may standard size 4” x 9” describing what I do. I don’t know if this would be considered a flyer. I rearrange, redesign and stage houses for the owner or to sell.

```html
<!DOCTYPE html>
<html lang="en">
<head>
<meta charset="utf-8">
<title>Lorna Pettibone – Nook Charmer card</title>
<link href="https://fonts.googleapis.com/css2?family=Raleway:ital,wght@0,300;0,400;0,600;0,700;1,700&display=swap" rel="stylesheet">
<style>
  :root {
    --backdrop: #1b1b1b;
    --card-white: #ffffff;
    --slate: #858585;
    --ink: #1f1f1f;
    --terracotta: #d9875a;
    --adobe-dark: #7a4a30;
    --band: rgba(255,255,255,0.5);
  }
  html, body {
    margin: 0;
    width: 1189px;
    height: 1200px;
    overflow: hidden;
    background: var(--backdrop);
    font-family: "Raleway", sans-serif;
  }
  .card {
    position: absolute;
    left: 169px;
    width: 851px;
    height: 379px;
    background: var(--card-white);
  }
  .card--front { top: 195px; }
  .card--back  { top: 609px; }
  .card__panel {
    position: absolute;
    left: 19px;
    top: 19px;
    width: 813px;
    height: 341px;
    display: block;
  }
  .name { font-weight: 700; font-size: 25px; fill: var(--card-white); }
  .title, .award { font-weight: 300; font-size: 19px; fill: var(--card-white); }
  .contact { font-weight: 400; font-size: 18px; fill: var(--card-white); }
  .pitch { font-weight: 300; font-size: 27px; fill: var(--ink); }
  .pitch--strong { font-weight: 700; }
  .back-text { font-size: 19px; fill: var(--card-white); font-weight: 400; letter-spacing: 0.6px; }
  .back-text--quote { font-style: italic; font-weight: 700; }
  .back-text--bold { font-weight: 700; }
  .tagline { font-weight: 600; font-size: 19px; letter-spacing: 2.5px; fill: var(--card-white); }
</style>
</head>
<body>

<section class="card card--front">
  <svg class="card__panel" viewBox="0 0 997 416" preserveAspectRatio="none">
    <defs>
      <linearGradient id="houseTones" x1="0" y1="0" x2="0" y2="1">
        <stop offset="0" stop-color="#8a6a55"/>
        <stop offset="0.35" stop-color="#d9875a"/>
        <stop offset="0.75" stop-color="#b9745a"/>
        <stop offset="1" stop-color="#7a5a48"/>
      </linearGradient>
      <radialGradient id="portraitTones" cx="0.5" cy="0.45" r="0.6">
        <stop offset="0" stop-color="#d9b3a3"/>
        <stop offset="0.6" stop-color="#9c7d6c"/>
        <stop offset="1" stop-color="#5b4a40"/>
      </radialGradient>
    </defs>
    <rect class="house-photo" x="0" y="100" width="997" height="316" fill="url(#houseTones)" role="img" aria-label="Photo of an adobe-style terracotta house at dusk with mountains behind"/>
    <path class="header-band" d="M0,0 H997 V123 C800,100 600,180 380,193 L0,166 Z" fill="var(--slate)"/>
    <path class="wave-line" d="M380,193 C600,180 800,100 997,123" fill="none" stroke="#ffffff" stroke-width="4"/>
    <path class="wave-line" d="M0,166 L60,176" fill="none" stroke="#ffffff" stroke-width="4"/>
    <rect class="pitch-band" x="410" y="278" width="587" height="115" fill="var(--band)"/>
    <circle class="portrait" cx="210" cy="219" r="166" fill="url(#portraitTones)" stroke="#ffffff" stroke-width="4" role="img" aria-label="Portrait photo of Lorna Pettibone"/>

    <text class="name" x="963" y="48" text-anchor="end">LORNA PETTIBONE</text>
    <text class="title" x="963" y="68" text-anchor="end">Nook Charmer</text>
    <text class="award" x="963" y="100" text-anchor="end">As a Hearth &amp; Garden Living National Award Winner</text>

    <text class="contact" x="963" y="159" text-anchor="end">lorna.pettibone@mailnook.net</text>
    <text class="contact" x="963" y="182" text-anchor="end">555-204-3187</text>
    <text class="contact" x="963" y="206" text-anchor="end">4120 W. Juniper Lane Mesa Verde, AZ 85000</text>

    <text class="pitch" x="963" y="310" text-anchor="end">WITH LITTLE OR NO COST,</text>
    <text class="pitch pitch--strong" x="963" y="345" text-anchor="end">LORNA BREATHES</text>
    <text class="pitch" x="963" y="380" text-anchor="end">NEW LIFE &amp; ENERGY INTO YOUR HOME.</text>
  </svg>
</section>

<section class="card card--back">
  <svg class="card__panel" viewBox="0 0 997 417" preserveAspectRatio="none">
    <defs>
      <linearGradient id="fadedHouse" x1="0" y1="0" x2="0" y2="1">
        <stop offset="0" stop-color="#878787"/>
        <stop offset="0.5" stop-color="#8a7d77"/>
        <stop offset="1" stop-color="#7e7a78"/>
      </linearGradient>
    </defs>
    <rect x="0" y="0" width="997" height="417" fill="url(#fadedHouse)" role="img" aria-label="Faded photo of the adobe house behind a grey overlay"/>
    <text class="back-text" x="498" y="88" text-anchor="middle">Thrilled Customers Say...</text>
    <text class="back-text back-text--quote" x="498" y="110" text-anchor="middle">“ This is just how I dreamed my home would look!”</text>
    <text class="back-text" x="498" y="164" text-anchor="middle">For 36 years, Lorna was a real estate Broker in Oregon. She has record of</text>
    <text class="back-text" x="498" y="187" text-anchor="middle">transformimg houses thet do not sell into homes that sell quickly.</text>
    <text class="back-text" x="498" y="248" text-anchor="middle">Make your space livable, lovable and <tspan class="back-text--bold">profitable...</tspan></text>
    <text class="back-text" x="498" y="271" text-anchor="middle">...a place whwer you or your buyer can hardly wait to com home to.</text>
    <text class="back-text" x="498" y="293" text-anchor="middle">Voila!</text>
    <text class="tagline" x="498" y="362" text-anchor="middle">REARRANGED. REDESIGNED. STAGED TO SELL</text>
  </svg>
</section>

</body>
</html>
```